Looking for potential sellers

We help people buy and sell homes and are currently looking for potential home sellers. We offer low commissions, are the Local Colorado Springs and Falcon Experts, homes selling fast and at top dollar, Free expert pricing opinions and Consultations, over 9 years of experience, top rated Realtors creative and aggressive marketing strategies. Never merely own a house, THRIVE at Harborview. phone number 482-630-9157 web thriveatharborview.com

```html
<!DOCTYPE html>
<html lang="en">
<head>
<meta charset="utf-8">
<title>Keystone Realty – Seller Postcard</title>
<link href="https://fonts.googleapis.com/css2?family=PT+Sans+Narrow:wght@400;700&family=Open+Sans:wght@400;600&family=Arimo:ital,wght@0,400;0,700;1,400&display=swap" rel="stylesheet">
<style>
  :root{
    --olive:#a09a2c;
    --navy:#0f1a26;
    --white:#ffffff;
    --ink:#1d1d1d;
    --stage:#cacaca;
    --photo-a:#b69e8c;
    --photo-b:#8a705f;
  }
  *{box-sizing:border-box;margin:0;padding:0}
  html,body{width:1000px;height:1200px;overflow:hidden;background:var(--stage)}
  body{position:relative;font-family:"PT Sans Narrow",sans-serif}
  .card{position:absolute;left:143px;width:717px;background:var(--white);overflow:hidden}
  .card--front{top:97px;height:480px}
  .card--back{top:617px;height:477px}
  .card__shapes{position:absolute;inset:0;width:100%;height:100%}
  .abs{position:absolute}

  /* front */
  .portrait{left:0;top:43px;width:400px;height:437px;background:linear-gradient(135deg,var(--photo-a),var(--photo-b));clip-path:polygon(0 0,305px 0,385px 317px,302px 317px,302px 437px,0 437px)}
  .brand{display:flex;align-items:center;gap:10px;color:var(--navy);font-family:"PT Sans Narrow",sans-serif;font-weight:700;white-space:nowrap}
  .brand__mark{width:16px;height:16px;background:var(--olive)}
  .brand--front{left:470px;top:84px;font-size:34px}
  .headline{left:404px;top:180px;color:var(--white);font-weight:700;font-size:48px;line-height:1}
  .subline{right:80px;top:246px;color:var(--white);font-size:21px;line-height:1}
  .subline b{font-weight:700}
  .statement{right:24px;top:272px;color:var(--white);font-size:37px;line-height:1;white-space:nowrap}
  .statement b{font-weight:700}
  .tagline{left:272px;top:359px;line-height:28px;color:var(--white);font-family:"Open Sans",sans-serif;font-size:19px;letter-spacing:.3px;white-space:nowrap}
  .agent{left:318px;top:408px;text-align:right;font-family:"Arimo",sans-serif;color:var(--ink);line-height:1.2}
  .agent__name{font-weight:700;font-size:19px}
  .agent__title{font-style:italic;font-size:19px}
  .contact-url{left:480px;top:400px;font-size:23px;color:var(--ink)}
  .contact-phone{left:480px;top:424px;font-size:39px;font-weight:700;color:var(--olive);line-height:1}

  /* back */
  .offer-title{left:16px;top:20px;color:var(--white);font-weight:400;font-size:46px;line-height:1}
  .offer-title b{font-weight:700}
  .offer-list{left:16px;top:73px;list-style:none;color:var(--white);font-weight:700;font-size:16px;text-transform:uppercase;line-height:24px}
  .offer-list li{display:flex;gap:8px}
  .offer-list svg{flex:none;margin-top:5px}
  .testimonial{left:22px;width:296px;color:var(--white);font-family:"PT Sans Narrow",sans-serif;font-size:11px;line-height:1.4}
  .testimonial__by{margin-top:3px;text-align:center;font-weight:700;font-size:13px;line-height:1.2;color:var(--white)}
  .testimonial__by span{font-weight:400;font-style:italic;font-size:10px;color:var(--olive)}
  .cta{left:22px;top:439px;color:var(--white);font-size:18px;line-height:1}
  .cta-phone{left:162px;top:433px;width:153px;height:32px;background:var(--white);color:var(--navy);font-weight:700;font-size:24px;text-align:center;line-height:32px}
  .vertical-url{left:258px;top:343px;width:220px;height:24px;line-height:24px;transform:rotate(-78deg);color:var(--white);font-size:19px;text-align:center;white-space:nowrap}
  .indicia{left:620px;top:20px;width:70px;border:1px solid #777;font-family:"Arimo",sans-serif;font-size:6.5px;line-height:1.35;text-align:center;padding:3px 0;color:#333}
  .address{left:532px;top:92px;width:158px;border:1px solid #777;font-family:"Arimo",sans-serif;font-size:7px;line-height:1.3;padding:3px 8px;color:#333}
  .address__line1{text-align:center;margin-bottom:4px}
  .brand--back{left:420px;top:410px;font-size:26px}
</style>
</head>
<body>

<section class="card card--front">
  <div class="abs portrait" role="img" aria-label="Portrait photograph of the realtor"></div>
  <svg class="card__shapes" viewBox="0 0 717 480" aria-hidden="true">
    <polygon points="0,23 232,23 242,42 0,42" fill="var(--olive)"/>
    <polygon points="335,118 432,118 442,148 345,148" fill="var(--navy)"/>
    <polygon points="347,148 717,148 717,358 402,358" fill="var(--olive)"/>
    <line x1="335" y1="150" x2="392" y2="352" stroke="var(--navy)" stroke-width="2"/>
    <line x1="440" y1="326" x2="690" y2="324" stroke="var(--white)" stroke-width="3"/>
    <polygon points="300,355 717,355 717,388 267,388" fill="var(--navy)"/>
    <rect x="302" y="394" width="415" height="3" fill="var(--olive)"/>
    <rect x="302" y="464" width="415" height="4" fill="var(--olive)"/>
    <line x1="440" y1="405" x2="440" y2="458" stroke="#888" stroke-width="1"/>
    <g fill="none" stroke="var(--ink)" stroke-width="1.6">
      <circle cx="457" cy="416" r="10"/>
      <ellipse cx="457" cy="416" rx="4.5" ry="10"/>
      <line x1="447" y1="416" x2="467" y2="416"/>
      <circle cx="457" cy="446" r="10"/>
    </g>
    <path d="M452 441 l3 -1 2 4 -2 2 q2 4 5 5 l2 -2 4 2 -1 3 q-8 1 -13 -13z" fill="var(--ink)"/>
  </svg>

  <div class="abs brand brand--front"><span class="brand__mark"></span>Keystone Realty</div>
  <h1 class="abs headline">It's Time...</h1>
  <p class="abs subline">Never Merely <b>Own</b> a House,</p>
  <p class="abs statement"><b>THRIVE</b> at Harborview.</p>
  <p class="abs tagline">We help people buy and sell homes .</p>
  <div class="abs agent">
    <div class="agent__name">Dale Mercer</div>
    <div class="agent__title">REALTOR®</div>
  </div>
  <p class="abs contact-url">www.thriveatharborview.com</p>
  <p class="abs contact-phone">482-630-9157</p>
</section>

<section class="card card--back">
  <svg class="card__shapes" viewBox="0 0 717 477" aria-hidden="true">
    <polygon points="0,0 432,0 326,477 0,477" fill="var(--olive)"/>
    <polygon points="440,0 450,0 360,477 330,477" fill="var(--navy)"/>
    <rect x="186" y="49" width="172" height="11" fill="var(--navy)"/>
    <polygon points="0,250 356,250 322,423 0,423" fill="var(--navy)"/>
    <g fill="none" stroke="var(--olive)" stroke-width="1">
      <rect x="14" y="262" width="308" height="56"/>
      <rect x="14" y="332" width="308" height="66"/>
    </g>
    <circle cx="318" cy="236" r="7" fill="var(--white)"/>
    <circle cx="336" cy="236" r="7" fill="var(--white)"/>
  </svg>

  <h2 class="abs offer-title">WE <b>OFFER</b></h2>
  <ul class="abs offer-list">
    <li><svg width="13" height="13" viewBox="0 0 13 13"><rect x=".75" y=".75" width="11.5" height="11.5" fill="none" stroke="#fff" stroke-width="1.5"/><path d="M3 6.5l2.5 2.5L10.5 3" fill="none" stroke="#fff" stroke-width="1.6"/></svg>Low commissions,</li>
    <li><svg width="13" height="13" viewBox="0 0 13 13"><rect x=".75" y=".75" width="11.5" height="11.5" fill="none" stroke="#fff" stroke-width="1.5"/><path d="M3 6.5l2.5 2.5L10.5 3" fill="none" stroke="#fff" stroke-width="1.6"/></svg>Local Colorado Springs and Falcon Experts, Homes</li>
    <li><svg width="13" height="13" viewBox="0 0 13 13"><rect x=".75" y=".75" width="11.5" height="11.5" fill="none" stroke="#fff" stroke-width="1.5"/><path d="M3 6.5l2.5 2.5L10.5 3" fill="none" stroke="#fff" stroke-width="1.6"/></svg>Selling fast and at top dollar,</li>
    <li><svg width="13" height="13" viewBox="0 0 13 13"><rect x=".75" y=".75" width="11.5" height="11.5" fill="none" stroke="#fff" stroke-width="1.5"/><path d="M3 6.5l2.5 2.5L10.5 3" fill="none" stroke="#fff" stroke-width="1.6"/></svg>Free expert pricing opinions and consultations,</li>
    <li><svg width="13" height="13" viewBox="0 0 13 13"><rect x=".75" y=".75" width="11.5" height="11.5" fill="none" stroke="#fff" stroke-width="1.5"/><path d="M3 6.5l2.5 2.5L10.5 3" fill="none" stroke="#fff" stroke-width="1.6"/></svg>Over 9 years of experience,</li>
    <li><svg width="13" height="13" viewBox="0 0 13 13"><rect x=".75" y=".75" width="11.5" height="11.5" fill="none" stroke="#fff" stroke-width="1.5"/><path d="M3 6.5l2.5 2.5L10.5 3" fill="none" stroke="#fff" stroke-width="1.6"/></svg>Top rated realtors creative and aggressive<br>marketing strategies.</li>
  </ul>

  <div class="abs testimonial" style="top:270px">
    <p>Dale Morgan is one of the best Realtors in Colorado Springs! Thank you for the quick sale of our home and for all that you did for us!</p>
    <p class="testimonial__by">Marissa- <span>KRG Client</span></p>
  </div>
  <div class="abs testimonial" style="top:338px">
    <p>Dale is absolutely the best. Selling our home was so much easier with him as our realtor. He is always there to answer questions no matter how small. I would definitely recommend him!</p>
    <p class="testimonial__by">Carla Jennings <span>– KRG Client - 4/13/2015</span></p>
  </div>

  <p class="abs cta">Get in touch with us</p>
  <p class="abs cta-phone">482-630-9157</p>
  <p class="abs vertical-url">www.thriveatharborview.com</p>

  <div class="abs indicia">PRSRT STD<br>ECRWSS<br>U.S. POSTAGE<br>PAID<br>EDDM RETAIL</div>
  <div class="abs address">
    <p class="address__line1">*********ECRWSSEDDM****</p>
    <p>Local<br>Postal Customer<br>City, State 5-Digit ZIP Code</p>
  </div>
  <div class="abs brand brand--back"><span class="brand__mark"></span>Keystone Realty</div>
</section>

</body>
</html>
```